Motion Nest Business Cards

Can all designers please apply the following info on their designs' back-side of the business card: (please see brief file upload ('Info for backside...' - for required info, colours & layout)

SPECIALISING IN INDIVIDUAL PILATES INSTRUCTION
MATWORK – including small apparatus
and STUDIO:
VIVANTE 3 GLIDER
LADDER BARREL
COUNTOUR BARREL
FLEXI DOME
VIM STOOL
KIM-O-LAN

Business Cards for Motion Nest - applying the Motion Nest logo design selected earlier.
Note the business card requires both a front and back side. Please refer to two uploaded ppt-files for type of info required to be displayed, and rough position of where info could be. Require innovative / fresh approach to business card design and use of colour by designers now. Please refer to and use logo as uploaded - also for potential business card colour application.

Dear Designers,

Please note the additional inclusion / upload of two draft ppt-files that try to show where I want what type of information, for both the front & back sides of the required business card, plus an attempt at showing the high-level concept / idea of business info position.

As my 'drafts' obviously lack colour and any ability towards innovative card design or approach – I now rely on your vastly superior graphic design abilities to produce a really great business card for my business…

Looking forward to your submissions!

Kind regards, Merika for: Motion Nest 

Hello all Designers,

Can all designers please apply the following info on their designs' back-side of the business card: (please see / refer to the Brief and specifically the file upload ('Info for backside...' - for required info, colours & layout) - for the backside of the business card).

Info content (without colour, layout etc.):

and STUDIO:

VIVANTE 3 GLIDER

LADDER BARREL

COUNTOUR BARREL

FLEXI DOME

VIM STOOL

KIM-O-LAN

Thank you to all designers that submitted for consideration!

With regards,

Motion Nest

```html
<!DOCTYPE html>
<html lang="en">
<head>
<meta charset="utf-8">
<title>Motion Nest Business Cards</title>
<link rel="stylesheet" href="https://fonts.googleapis.com/css2?family=PT+Sans:wght@400;700&display=swap">
<style>
  :root {
    --page-bg: #e4e4e4;
    --card-front: #fbfbf9;
    --card-back: #cddcaa;
    --green: #3f5f13;
    --orange: #d9531e;
    --shadow: rgba(0,0,0,0.18);
  }
  * { box-sizing: border-box; margin: 0; padding: 0; }
  html, body {
    width: 1200px; height: 900px; overflow: hidden;
    background: var(--page-bg);
    font-family: "PT Sans", Arial, sans-serif;
  }
  .stage {
    position: relative; width: 1200px; height: 900px;
  }
  .card {
    position: absolute; top: 285px;
    width: 540px; height: 330px;
    box-shadow: 0 8px 24px var(--shadow);
  }
  /* back side */
  .card-back { left: 40px; background: var(--card-back); text-align: center; }
  .back-brand {
    display: flex; align-items: center; justify-content: center; gap: 10px;
    margin-top: 38px;
    color: var(--green); font-size: 30px; font-weight: 400;
  }
  .brand-dot { width: 20px; height: 20px; border-radius: 50%; background: var(--green); }
  .specialty {
    margin-top: 28px;
    color: var(--orange); font-weight: 700; font-size: 17px; letter-spacing: 0.2px;
  }
  .matwork {
    margin-top: 14px; color: var(--green); font-size: 15px;
  }
  .apparatus-list {
    list-style: none; margin-top: 6px;
    color: var(--green); font-size: 15px; line-height: 21px;
  }
  .apparatus-list li::before {
    content: "•"; color: var(--orange); margin-right: 8px;
  }
  /* front side */
  .card-front { left: 620px; background: var(--card-front); }
  .holder-name {
    position: absolute; left: 34px; top: 30px;
    color: var(--green); font-size: 29px; letter-spacing: 0.3px;
  }
  .holder-title {
    position: absolute; left: 34px; top: 68px;
    color: var(--orange); font-size: 15.5px;
  }
  .contact {
    position: absolute; left: 34px; top: 116px;
    color: var(--green); font-size: 15.5px; line-height: 24px;
  }
  .contact-row { display: flex; align-items: center; gap: 12px; }
  .contact-row svg { width: 12px; height: 12px; }
  .studio {
    position: absolute; left: 34px; top: 192px;
    color: var(--green); font-size: 15.5px; line-height: 20px;
  }
  .studio-label { color: var(--orange); font-weight: 700; }
  .rule { position: absolute; height: 2px; background: var(--orange); }
  .rule-left { left: 0; top: 268px; width: 300px; }
  .rule-right { right: 0; top: 300px; width: 30px; }
  .front-brand {
    position: absolute; right: 30px; top: 178px;
    display: flex; align-items: center; gap: 10px;
    color: var(--orange); font-size: 42px; line-height: 1;
  }
  .front-brand .brand-dot { background: var(--green); width: 22px; height: 22px; }
  .tagline {
    position: absolute; right: 30px; top: 232px;
    color: var(--orange); font-size: 14.5px; letter-spacing: 0.4px;
  }
  .tagline .sep { color: var(--green); }
  .website {
    position: absolute; right: 44px; top: 268px;
    color: var(--green); font-size: 16px;
  }
</style>
</head>
<body>
<main class="stage">

  <section class="card card-back" aria-label="Card back">
    <div class="back-brand"><span class="brand-dot"></span>Motion Nest</div>
    <p class="specialty">SPECIALISING IN INDIVIDUAL PILATES INSTRUCTION</p>
    <p class="matwork">MATWORK &nbsp;– including small apparatus and STUDIO:</p>
    <ul class="apparatus-list">
      <li>VIVANTE 3 GLIDER</li>
      <li>LADDER BARREL</li>
      <li>COUNTOUR BARREL</li>
      <li>FLEXI DOME</li>
      <li>VIM STOOL</li>
      <li>KIM-O-LAN</li>
    </ul>
  </section>

  <section class="card card-front" aria-label="Card front">
    <h1 class="holder-name">Merika Hollowell</h1>
    <p class="holder-title">Diploma of Professional Pilates Instruction</p>

    <div class="contact">
      <div class="contact-row">
        <svg viewBox="0 0 12 12" aria-hidden="true"><rect x="3" y="0.5" width="6" height="11" rx="1" fill="none" stroke="#d9531e" stroke-width="1.2"/><line x1="5" y1="9.5" x2="7" y2="9.5" stroke="#d9531e"/></svg>
        <span>041 555 0192</span>
      </div>
      <div class="contact-row">
        <svg viewBox="0 0 12 12" aria-hidden="true"><rect x="0.6" y="2" width="10.8" height="8" fill="none" stroke="#d9531e" stroke-width="1.2"/><polyline points="0.6,2 6,7 11.4,2" fill="none" stroke="#d9531e" stroke-width="1.2"/></svg>
        <span>info@motionnest.com.au</span>
      </div>
    </div>

    <div class="studio">
      <div class="studio-label">Studio location</div>
      <div>12 Larkspur Avenue</div>
      <div>Elmvale WA 6040</div>
    </div>

    <div class="rule rule-left"></div>

    <div class="front-brand"><span class="brand-dot"></span>Motion Nest</div>
    <p class="tagline">BALANCE <span class="sep">•</span> STRENGTH <span class="sep">•</span> FLEXIBILITY</p>
    <p class="website">www.motionnest.com.au</p>

    <div class="rule rule-right"></div>
  </section>

</main>
</body>
</html>
```